名刺の背景は、白地(裏地デザインは、ありもOK)
複数の色味というよりは、シンプルな色使い

シンプルだけど、上品さを感じるもの

株式会社plumeridge/代表取締役/名前/読みがな(英語)/住所/電話番号/mail address/HP URL
シンプル 複雑
単色 カラフル
暗い 明るい
日常 高級
遊び心 厳粛
未来的 伝統的
女性的 男性的
緑系、グレー系、色は絶対ではありませんので、イメージやデザインに添ってご提案いただけるのであれば嬉しいです
• 高解像度JPG (.jpg)
• イラストレーター形式 (.ai)
• フォトショップ形式 (.psd)
• PNG形式 (.png)
現在の色味が、添付ファイルの名刺の色なので、参考にしていただけると嬉しいです。
緑というよりは、エメラルドグリーンのような色味です。
※添付ファイルに記載されている、個人情報は名刺サンプルに記載しないでください。
お手数ですがよろしくお願いいたします。
※社名は「株式会社plumeridge」のみで、「inc.」は無しでお願いいたします。
たくさんのご提案ありがとうございます!
デザインが一般企業よりのものを探しており、可能であれば、
もう少しデザインを拝見したく、延長させていただきました。

お忙しいところお手数ですが、どうぞよろしくお願いいたします。

デザイン性が一番高かったためです。

たくさんのご提案、ありがとうございました!
ご丁寧にご対応いただき、とても助かりました。
また依頼あれば出させていただきます。

```html
<!DOCTYPE html>
<html lang="ja">
<head>
<meta charset="utf-8">
<title>plumeridge business card</title>
<link rel="stylesheet" href="https://fonts.googleapis.com/css2?family=Noto+Sans+JP:wght@400;500&family=Inconsolata:wght@400&display=swap">
<style>
  :root {
    --emerald: #2eb6b1;
    --paper: #ffffff;
    --page: #ffffff;
    --ink-soft: #7a8a8a;
    --shadow: rgba(0, 0, 0, 0.18);
  }
  * { margin: 0; padding: 0; box-sizing: border-box; }
  html, body {
    width: 844px; height: 1200px; overflow: hidden;
    background: var(--page);
    font-family: "Noto Sans JP", sans-serif;
  }
  .sheet { position: relative; width: 844px; height: 1200px; }
  .card {
    position: absolute; left: 160px; width: 530px; height: 320px;
    background: var(--paper);
    box-shadow: 0 1px 4px var(--shadow);
  }
  .card--front { top: 273px; }
  .card--back { top: 625px; }

  .front-band {
    position: absolute; left: 0; right: 0; top: 28px; height: 252px;
    background: var(--emerald);
    display: flex; flex-direction: column; align-items: center; justify-content: center;
    gap: 22px;
  }
  .front-mark { width: 62px; height: 62px; background: var(--paper); }
  .front-name {
    color: var(--paper); font-size: 34px; font-weight: 400; letter-spacing: 1px;
  }

  .back-company {
    position: absolute; left: 18px; top: 55px;
    font-size: 9px; color: var(--emerald); letter-spacing: 0.5px;
  }
  .back-mark {
    position: absolute; left: 40px; top: 100px; width: 60px; height: 60px;
    background: var(--emerald);
  }
  .back-divider {
    position: absolute; left: 164px; top: 50px; width: 1px; height: 236px;
    background: var(--emerald);
  }
  .back-info { position: absolute; left: 209px; top: 50px; width: 296px; color: var(--emerald); }
  .role { font-size: 10px; letter-spacing: 1px; }
  .name { font-size: 19px; font-weight: 500; letter-spacing: 6px; margin-top: 12px; }
  .name-roman { font-family: "Inconsolata", monospace; font-size: 11px; margin-top: 3px; letter-spacing: 0.5px; }
  .name-rule { height: 1px; background: var(--emerald); margin-top: 6px; width: 196px; }
  .contact {
    list-style: none; margin-top: 40px;
    font-family: "Inconsolata", monospace; font-size: 11px; line-height: 19.5px; letter-spacing: 0.4px;
  }
  .contact-rule { height: 1px; background: var(--emerald); margin-top: 10px; width: 236px; }
</style>
</head>
<body>
<main class="sheet">
  <section class="card card--front" aria-label="Card front">
    <div class="front-band">
      <div class="front-mark"></div>
      <p class="front-name">plumeridge</p>
    </div>
  </section>

  <section class="card card--back" aria-label="Card back">
    <p class="back-company">株式会社plumeridge</p>
    <div class="back-mark"></div>
    <div class="back-divider"></div>
    <div class="back-info">
      <p class="role">代表取締役</p>
      <p class="name">佐藤 美咲</p>
      <p class="name-roman">Misaki Sato</p>
      <div class="name-rule"></div>
      <ul class="contact">
        <li>〒100-0005 東京都千代田区丸の内1-2-3</li>
        <li>1-2-3 Marunouchi, Chiyoda-ku, TOKYO</li>
        <li>TEL 03-1234-5678</li>
        <li>MAIL misaki@plumeridge.jp</li>
        <li>www.plumeridge.jp</li>
      </ul>
      <div class="contact-rule"></div>
    </div>
  </section>
</main>
</body>
</html>
```